Wayline Billboard Co Business Card Design

We have a newly created business and logo, but we now need business cards using the new logo.
We are an Australian based business, and we sell advertising space on trucks. The business cards will be seen by media buyers, direct advertisers, fleet owners and business people in general.
Our colours are very simple - black and a strong yellow, with some white. We have chosen the black and yellow for various reasons, but in particular because they are high contrast, and they also have a parallel with the number plates used on our roads, which is relevant to our product offering.
My initial thoughts:
Keep it simple and uncluttered
Use both sides
Our default is Century Gothic
I can provide logo files as required. We do not yet have a website, so I can't direct you there just yet. That may well be another project!
Target Market(s)
The business cards will be seen by media buyers, direct advertisers, fleet owners and business people in general.
Industry/Entity Type
Advertising
Look and feel
Each slider illustrates characteristics of the customer's brand and the style your logo design should communicate.

```html
<!DOCTYPE html>
<html lang="en">
<head>
<meta charset="utf-8">
<title>Wayline Billboard Co — Business Card</title>
<link rel="stylesheet" href="https://fonts.googleapis.com/css2?family=Rubik:wght@400;500;700&display=swap">
<style>
  :root {
    --card-black: #050505;
    --brand-yellow: #e6e21c;
    --ink-white: #f2f2f2;
    --page-bg: #e9e6e1;
  }
  * { box-sizing: border-box; margin: 0; padding: 0; }
  html, body {
    width: 1200px; height: 880px; overflow: hidden;
    background: var(--page-bg);
    font-family: "Rubik", sans-serif;
  }
  .sheet {
    width: 1200px; height: 880px;
    display: flex; align-items: center; justify-content: center; gap: 44px;
  }
  .card {
    position: relative;
    width: 530px; height: 303px;
    background: var(--card-black);
    box-shadow: 0 10px 26px rgba(0,0,0,.18);
    overflow: hidden;
  }

  /* Front */
  .card-front .brand-name {
    position: absolute; left: 0; right: 0; top: 98px;
    text-align: center;
    color: var(--brand-yellow);
    font-weight: 700; font-size: 36px; letter-spacing: .5px;
    display: flex; align-items: center; justify-content: center; gap: 14px;
  }
  .brand-dot {
    width: 18px; height: 18px; border-radius: 50%;
    background: var(--brand-yellow);
  }
  .card-front .web {
    position: absolute; left: 0; right: 0; bottom: 32px;
    text-align: center;
    color: var(--brand-yellow);
    font-size: 15px; letter-spacing: 1.6px;
  }
  .card-front .web b { font-weight: 700; }

  /* Back */
  .card-back .brand-name {
    position: absolute; left: 28px; top: 30px;
    color: var(--brand-yellow);
    font-weight: 700; font-size: 19px;
    display: flex; align-items: center; gap: 9px;
  }
  .card-back .brand-name .brand-dot { width: 11px; height: 11px; }
  .contact {
    position: absolute; right: 30px; top: 72px; width: 230px;
    text-align: right; color: var(--ink-white);
  }
  .person-name {
    color: var(--brand-yellow); font-weight: 700; font-size: 22px; line-height: 26px;
  }
  .person-role { font-size: 13px; line-height: 16px; margin-top: 2px; }
  .rule { height: 1px; background: var(--brand-yellow); margin: 9px 0; }
  .contact-list { list-style: none; }
  .contact-list li {
    display: flex; justify-content: flex-end; align-items: center; gap: 8px;
    font-size: 12.5px; line-height: 19px;
  }
  .icon { width: 11px; height: 11px; fill: var(--brand-yellow); flex: none; }
  .address {
    display: flex; justify-content: flex-end; align-items: center; gap: 8px;
    font-size: 12.5px; line-height: 18px;
  }
  .address .icon { width: 12px; height: 15px; }
</style>
</head>
<body>
<main class="sheet">
  <section class="card card-front" aria-label="Card front">
    <div class="brand-name"><span class="brand-dot"></span>Wayline Billboard Co</div>
    <p class="web">www.<b>waylinebillboard</b>.au</p>
  </section>

  <section class="card card-back" aria-label="Card back">
    <div class="brand-name"><span class="brand-dot"></span>Wayline Billboard Co</div>
    <div class="contact">
      <p class="person-name">Dan Whitfield</p>
      <p class="person-role">Founder</p>
      <div class="rule"></div>
      <ul class="contact-list">
        <li>1800 555 019
          <svg class="icon" viewBox="0 0 12 12"><path d="M2.5 1h2l1 2.7-1.3 1a6.5 6.5 0 0 0 3.1 3.1l1-1.3L11 7.5v2a1.5 1.5 0 0 1-1.5 1.5A8.5 8.5 0 0 1 1 2.5 1.5 1.5 0 0 1 2.5 1z"/></svg></li>
        <li>+61 4 0000 5128
          <svg class="icon" viewBox="0 0 12 12"><path d="M3.5 0h5A1 1 0 0 1 9.5 1v10a1 1 0 0 1-1 1h-5a1 1 0 0 1-1-1V1a1 1 0 0 1 1-1zm.5 1.5v7.5h4V1.5zM6 9.8a.7.7 0 1 0 0 1.4.7.7 0 0 0 0-1.4z"/></svg></li>
        <li>dan@waylinebillboard.au
          <svg class="icon" viewBox="0 0 12 12"><path d="M0 2h12v8H0zm1 1v.4l5 3.3 5-3.3V3zm0 1.6V9h10V4.6L6 7.9z"/></svg></li>
        <li>www.waylinebillboard.au
          <svg class="icon" viewBox="0 0 12 12"><path d="M6 0a6 6 0 1 0 0 12A6 6 0 0 0 6 0zm0 1c.6 0 1.4 1.3 1.6 3.5H4.4C4.6 2.3 5.4 1 6 1zM1.1 5.5h2.3c0 1.3.2 2.4.6 3.4A5 5 0 0 1 1.1 5.5zm0-1A5 5 0 0 1 4 1.6c-.4 1-.6 1.9-.6 2.9zm3.3 1h3.2C7.5 8.2 6.7 11 6 11s-1.5-2.8-1.6-5.5zm4.2 0h2.3A5 5 0 0 1 8 8.9c.4-1 .6-2.1.6-3.4zm0-1c0-1-.2-1.9-.6-2.9a5 5 0 0 1 2.9 2.9z"/></svg></li>
      </ul>
      <div class="rule"></div>
      <div class="address">
        <span>PO Box 4410<br>Harbourside NSW 2199</span>
        <svg class="icon" viewBox="0 0 12 15"><path d="M6 0a5.5 5.5 0 0 0-5.5 5.5C.5 9.5 6 15 6 15s5.5-5.5 5.5-9.5A5.5 5.5 0 0 0 6 0zm0 7.8a2.3 2.3 0 1 1 0-4.6 2.3 2.3 0 0 1 0 4.6z"/></svg>
      </div>
    </div>
  </section>
</main>
</body>
</html>
```